Book Chapter Illustration Design Project

I need to get 8-10 illustrations done for each chapter of a book that my client has written
1. Introduction
2. Running Gears
3. The Training Plan
4. The Race
5. Injury Management
6. How to Keep it going
7. Runners keynotes
8. Frequently asked questions
The title of the book is 'Kettle Hill Morning', written by Marco Davin Quilapang from the Philippines.
Just think that finding running has changed his life and he wants that represented on the cover somehow with the title standing for both taking one more step with running and a metaphor for life.
I have attached an early version of the book for inspiration.
Note: This price is for the first design, the following designs will be at 50USD each

```html
<!DOCTYPE html>
<html lang="en">
<head>
<meta charset="UTF-8">
<title>Chapter I – Introduction</title>
<link href="https://fonts.googleapis.com/css2?family=Tinos:wght@400&display=swap" rel="stylesheet">
<style>
  :root {
    --backdrop: #cdcbab;
    --paper: #ffffff;
    --ink: #1a1a1a;
    --art-light: #f4f4f2;
    --art-mid: #d9d9d6;
  }
  html, body {
    margin: 0;
    padding: 0;
    width: 1200px;
    height: 900px;
    overflow: hidden;
    background: var(--backdrop);
  }
  .canvas {
    position: relative;
    width: 1200px;
    height: 900px;
    background: var(--backdrop);
  }
  .page {
    position: absolute;
    left: 344px;
    top: 30px;
    width: 512px;
    height: 840px;
    background: var(--paper);
    font-family: "Tinos", "Times New Roman", serif;
    color: var(--ink);
  }
  .chapter-art {
    position: absolute;
    left: 6px;
    top: 0;
    width: 366px;
    height: 300px;
    background: linear-gradient(160deg, var(--art-light) 0%, var(--art-mid) 100%);
  }
  .chapter-heading {
    position: absolute;
    left: 0;
    top: 326px;
    width: 100%;
    text-align: center;
    margin: 0;
    font-weight: 400;
  }
  .chapter-number {
    display: block;
    font-size: 23px;
    line-height: 30px;
  }
  .chapter-title {
    display: block;
    font-size: 33px;
    line-height: 38px;
  }
  .chapter-body {
    position: absolute;
    left: 30px;
    top: 412px;
    width: 454px;
    font-size: 15.4px;
    line-height: 22px;
  }
  .chapter-body p {
    margin: 0 0 22px;
    text-align: justify;
  }
</style>
</head>
<body>
<div class="canvas">
  <article class="page">
    <div class="chapter-art" role="img" aria-label="Line illustration of two boys running along a path past a picket fence and a bush"></div>
    <h1 class="chapter-heading">
      <span class="chapter-number">Chapter I</span>
      <span class="chapter-title">Introduction</span>
    </h1>
    <div class="chapter-body">
      <p>The meaning of running varies from one person to another. It's the basic fundamentals of placing your feet in front of another; we will just lace up and hit the road. We grew up running around our block, neighborhood or in school with our mates and much later into our late teens.</p>
      <p>I am no different than most people in the streets. I was an active lad during my school days and had participated in various sporting discipline from track and field, badminton, soccer and swimming. I picked up long distance running and loving it!!!</p>
      <p>Most of the time when I was introduced to a runner, it was almost an instantaneous reply from him, 'I am just a beginner'. The statement 'beginner runner' may perceive a novice getting to know what is running. However, there are different levels to it. It could mean as a person with no prior experience in running or another trying his hand on his maiden foray into his 1st marathon. Below diagram show the top 10 reason why we took up running.</p>
    </div>
  </article>
</div>
</body>
</html>
```